Counseling Practice Business Card

I need a professional looking business card incorporating my new logo that was just completed. Card needs to incorporate my name and title, description of my specialty, my address, my phone number, my fax number, my email and my website URL. I need to be able to choose design on/with different paper colors and textures.
I do not have a lot of business card ideas so I am open to anything but I want bold,sharp, clear card without additional designs other than my logo (see attached file info). I am open to different color backgrounds or paper colors including black. I do not like traditional brackets around area codes in phone number or dashes between numbers in phone number. Am open to other ways of presenting including periods between numbers as appropriate. I do not know enough to know what I like yet but I want card to coordinate and work together with my logo. My practice emphasizes natural mental health interventions so any use of color (with background paper color or the blue and green in my logo) that elicits nature is nice. In addition to black, any natural brown or wood looking background might be desirable also. Most of the offerings so far look very similar and boring.

Target Market(s)

Potential therapy clients and other professionals

Contact Information for Business Card

Card information:
Marcus T. Whitfield, Ph.D.
Licensed Clinical Psychologist
Integrative Health Coach
4812 Ferndale Pkwy NW
Suite 730
Marlow Springs, GA 30412
(770) 555-0142 phone
(770) 555-0186 fax
drmarcuswhitfield@kelvora.com
pathbloomcounseling.com

Font styles to use
Serif
Sans Serif
Other font styles liked:
• anything that you think looks crisp, clear and easily readable

Requirements
Must have
• Any color used should coordinate with my logo design (see attached files).
• Card should be printed horizontally so top and bottom are longest sides of rectangle.
• Background color or paper color should complement and highlight logo. Do not like a white background. black, grey, brown or any color my logo would blend well with.
Nice to have
• I would like designer to utilize color to highlight letters/name or phone-fax-web symbols.
• Bottom edge of card could be highlighted if appropriate to an idea.
Should not have
• I would NOT want the card to have a pure white background at all.
• No clear cards.
• Cards should be oriented with long sides on bottom and top, NOT sides. DO NOT LIKE THIS THIN TALL ORIENTATION.

```html
<!DOCTYPE html>
<html lang="en">
<head>
<meta charset="utf-8">
<title>Pathbloom Counseling – Business Card</title>
<link href="https://fonts.googleapis.com/css2?family=Open+Sans:wght@400;600;700&display=swap" rel="stylesheet">
<style>
  :root {
    --backdrop: #e6e6e8;
    --kraft: #a98c68;
    --kraft-edge: #8f7554;
    --ink: #141414;
    --brand-blue: #2f7fce;
    --brand-green: #1f8a45;
  }
  * { box-sizing: border-box; margin: 0; padding: 0; }
  html, body { width: 1200px; height: 800px; overflow: hidden; }
  body {
    background: var(--backdrop);
    font-family: "Open Sans", Arial, sans-serif;
    color: var(--ink);
    display: flex;
    align-items: center;
    justify-content: center;
    gap: 40px;
  }
  .card {
    position: relative;
    width: 540px;
    height: 309px;
    background: var(--kraft);
    border-bottom: 4px solid var(--kraft-edge);
    border-radius: 2px;
    overflow: hidden;
  }
  .card-front {
    display: flex;
    flex-direction: column;
    align-items: center;
    justify-content: center;
    gap: 26px;
  }
  .brand-name {
    font-weight: 700;
    color: var(--brand-green);
    letter-spacing: 0.5px;
    white-space: nowrap;
  }
  .card-front .brand-name { font-size: 42px; }
  .front-url {
    color: var(--brand-blue);
    font-size: 17px;
    letter-spacing: 3px;
  }
  .card-back { padding: 34px 32px 0 32px; }
  .card-back .brand-name {
    position: absolute;
    top: 26px;
    right: 28px;
    font-size: 22px;
  }
  .holder-name {
    margin-top: 46px;
    font-size: 20px;
    font-weight: 600;
    line-height: 1.2;
  }
  .holder-title {
    color: var(--brand-blue);
    font-size: 14px;
    font-weight: 600;
    line-height: 1.3;
  }
  .rule {
    width: 80px;
    height: 3px;
    background: var(--brand-blue);
    margin: 14px 0 12px;
  }
  .contact-list { list-style: none; }
  .contact-list li {
    display: flex;
    align-items: center;
    gap: 10px;
    font-size: 13px;
    line-height: 20px;
  }
  .icon { width: 13px; height: 13px; flex: none; fill: var(--brand-green); }
  .address {
    display: flex;
    align-items: center;
    gap: 10px;
    font-size: 13px;
    margin-top: 16px;
    white-space: nowrap;
  }
</style>
</head>
<body>
  <section class="card card-front">
    <div class="brand-name">Pathbloom Counseling</div>
    <div class="front-url">pathbloomcounseling.com</div>
  </section>

  <section class="card card-back">
    <div class="brand-name">Pathbloom Counseling</div>
    <h1 class="holder-name">Marcus T. Whitfield, Ph.D.</h1>
    <p class="holder-title">Licensed Clinical Psychologist</p>
    <p class="holder-title">Integrative Health Coach</p>
    <div class="rule"></div>
    <ul class="contact-list">
      <li>
        <svg class="icon" viewBox="0 0 16 16" aria-hidden="true"><path d="M1 5c0-2 2-3 7-3s7 1 7 3v1h-4V4.5H5V6H1zM3 7h10l1 7H2z"/></svg>
        (770) 555-0142
      </li>
      <li>
        <svg class="icon" viewBox="0 0 16 16" aria-hidden="true"><path d="M4 1h7l1 1v4H4zM1 7h14v7H1z"/></svg>
        (770) 555-0186
      </li>
      <li>
        <svg class="icon" viewBox="0 0 16 16" aria-hidden="true"><rect x="1" y="3" width="14" height="10" rx="1"/></svg>
        drmarcuswhitfield@kelvora.com
      </li>
    </ul>
    <div class="rule"></div>
    <p class="address">
      <svg class="icon" viewBox="0 0 16 16" aria-hidden="true"><path d="M8 0a5.5 5.5 0 0 0-5.5 5.5C2.5 10 8 16 8 16s5.5-6 5.5-10.5A5.5 5.5 0 0 0 8 0zm0 8a2.5 2.5 0 1 1 0-5 2.5 2.5 0 0 1 0 5z"/></svg>
      4812 Ferndale Pkwy NW, Suite 730, Marlow Springs, GA 30412
    </p>
  </section>
</body>
</html>
```